Vital Spark Electrical in need of a business card design

We need a new business card designed for our electrical business. We have a logo already which I will attach below.
Would like the business card to be..
-BLACK background preferably, possibly white back ground behind logo if colours clash.
-White & Blue (logo blue) text
Something that makes the logo pop, & a modern look. Possibly minimal clean format.

REQUIRE:
-Logo on front & back

TEXT TO INCLUDE (ON ONE SIDE):

Tom Harlow
Director/Electrician
M: 0417 365 208
E:info@vitalsparkelectrical-example.com.au
W:www.vitalsparkelectrical-example.com.au
R.E.C 57318

Custom/New Homes
Renovations
Commercial Office/Shop Fit-outs
Communications & Security Cameras
Electric Vehicle Chargers
Airconditioning
Updates

Requirements
Nice to have
• Possibly even lighten the grey shades for the words 'Vital' & 'Spark' to be more easily read on a black background.

```html
<!DOCTYPE html>
<html lang="en">
<head>
<meta charset="utf-8">
<title>Vital Spark Electrical – Business Card</title>
<link rel="stylesheet" href="https://fonts.googleapis.com/css2?family=Roboto:wght@400;500;700&display=swap">
<style>
  :root {
    --backdrop: #3b3b3b;
    --card: #222222;
    --card-edge: #1a1a1a;
    --blue: #1b9ce2;
    --white: #f2f2f2;
    --grey: #b9bec4;
    --faint: #2b2b2b;
  }
  * { box-sizing: border-box; margin: 0; padding: 0; }
  html, body {
    width: 1200px; height: 1021px; overflow: hidden;
    background: var(--backdrop);
    font-family: "Roboto", Arial, sans-serif;
    color: var(--white);
  }
  .canvas {
    position: relative; width: 1200px; height: 1021px;
    display: flex; flex-direction: column; align-items: center; justify-content: center; gap: 56px;
  }
  .card {
    position: relative; width: 700px; height: 400px;
    background: var(--card);
    border: 1px solid var(--card-edge);
    box-shadow: 0 14px 30px rgba(0,0,0,.45);
    overflow: hidden;
  }
  .brand {
    display: flex; align-items: center; gap: 14px;
  }
  .brand-mark {
    width: 22px; height: 22px; background: var(--blue);
  }
  .brand-name {
    font-weight: 500; color: var(--grey); letter-spacing: .5px;
  }

  /* front: services */
  .card--front .brand {
    position: absolute; left: 0; right: 0; top: 130px; justify-content: center;
  }
  .card--front .brand-name { font-size: 40px; }
  .services {
    position: absolute; left: 30px; right: 30px; top: 262px;
    text-align: center; font-size: 17px; line-height: 1.5;
  }
  .services .sep { color: var(--blue); margin: 0 6px; }

  /* back: contact */
  .card--back .brand {
    position: absolute; left: 46px; top: 50px;
  }
  .card--back .brand-mark { width: 18px; height: 18px; }
  .card--back .brand-name { font-size: 30px; }
  .person {
    position: absolute; right: 60px; top: 150px; text-align: right;
  }
  .person-name {
    font-size: 22px; font-weight: 700; color: var(--blue); text-transform: uppercase; letter-spacing: .3px;
  }
  .person-role { font-size: 17px; margin-top: 2px; }
  .contact {
    position: absolute; left: 46px; bottom: 54px;
    list-style: none; font-size: 17px; line-height: 1.45;
  }
  .contact li { display: flex; align-items: center; gap: 8px; }
  .contact svg { width: 14px; height: 14px; flex: none; }
  .contact .licence { padding-left: 0; margin-top: 6px; }
  .backdrop-square {
    position: absolute; right: 40px; bottom: -40px; width: 240px; height: 240px;
    background: var(--faint);
  }
</style>
</head>
<body>
<main class="canvas">
  <section class="card card--front">
    <div class="brand">
      <span class="brand-mark"></span>
      <span class="brand-name">Vital Spark Electrical</span>
    </div>
    <p class="services">
      Custom/New Homes<span class="sep">|</span>Renovations<span class="sep">|</span>Commercial Office/Shop Fit-outs<br>
      Communications &amp; Security Cameras<span class="sep">|</span>Electric Vehicle Chargers<span class="sep">|</span>Airconditioning
    </p>
  </section>

  <section class="card card--back">
    <div class="backdrop-square"></div>
    <div class="brand">
      <span class="brand-mark"></span>
      <span class="brand-name">Vital Spark Electrical</span>
    </div>
    <div class="person">
      <p class="person-name">Tom Harlow</p>
      <p class="person-role">Director/Electrician</p>
    </div>
    <ul class="contact">
      <li>
        <svg viewBox="0 0 16 16" aria-hidden="true"><path d="M4 1l3 3-2 2c1 2 3 4 5 5l2-2 3 3-2 3C7 15 1 9 1 3z" fill="none" stroke="#1b9ce2" stroke-width="1.4"/></svg>
        0417 365 208
      </li>
      <li>
        <svg viewBox="0 0 16 16" aria-hidden="true"><rect x="1" y="3" width="14" height="10" fill="none" stroke="#1b9ce2" stroke-width="1.4"/><path d="M1 3l7 6 7-6" fill="none" stroke="#1b9ce2" stroke-width="1.4"/></svg>
        info@vitalsparkelectrical-example.com.au
      </li>
      <li>
        <svg viewBox="0 0 16 16" aria-hidden="true"><circle cx="8" cy="8" r="6.5" fill="none" stroke="#1b9ce2" stroke-width="1.3"/><path d="M1.5 8h13M8 1.5c-3 3-3 10 0 13M8 1.5c3 3 3 10 0 13" fill="none" stroke="#1b9ce2" stroke-width="1.1"/></svg>
        www.vitalsparkelectrical-example.com.au
      </li>
      <li class="licence">R.E.C 57318</li>
    </ul>
  </section>
</main>
</body>
</html>
```